Business card for Real Estate Company located in Coastal area of spain

Want a business card design. Simple, professional, horizontal layout. will be 2 sided. Name of company (logo big on front). Name of agent, phone and email address. Back side will be list of general services we provide. Would like to see 2 separate concepts using the 2 separate logo treatments. One using Rich dark, bright blue as the stock color, and the other using White as the stock color.
Logo files uploaded (2 different versions) Domain (harbourkeyestates.com) Moraira-Calpe-Altea-Javea-Denia-Marina Alta Area (perhaps across the bottom of the front of card0 Ingrid Tavel Licensed Estate Agent / Partner Ingrid@harbourkeyestates.com +34.611.48.27.09 Back of card should list services offered

Real Estate Sales and Investments Real Estate Rental Management Kitchen, Bathroom Reformations Complete Home Reformation Services Window and Door Replacement Landscape and Garden Management Pool and Jacuzzi Service

Target Market(s)

Real estate and construction

Industry/Entity Type

Real Estate

Contact Information for Business Card

Logo files uploaded (2 different versions) Domain (harbourkeyestates.com) Moraira-Calpe-Altea-Javea-Denia-Marina Alta Area (perhaps across the bottom of the front of card0 Ingrid Tavel Licensed Estate Agent / Partner Ingrid@harbourkeyestates.com +34.611.48.27.09

Colors

Designer to choose colors to be used in the design.

Requirements
Must have
• progressive look professional
Nice to have
• Front big logo, Agent details. Back, list of services included in project description
Should not have
• Gloss finish for card

```html
<!DOCTYPE html>
<html lang="en">
<head>
<meta charset="utf-8">
<title>Harbour Key Estates – Services</title>
<link rel="stylesheet" href="https://fonts.googleapis.com/css2?family=Open+Sans:wght@700&family=Montserrat:wght@300;400&display=swap">
<style>
  :root {
    --card-black: #000000;
    --wave-deep: #176f96;
    --wave-bright: #1ba7cf;
    --wave-white: #f4f1f1;
    --text-white: #ffffff;
    --guide-grey: #3a3a3a;
    --edge-grey: #eeeeee;
  }
  html, body {
    margin: 0;
    padding: 0;
    overflow: hidden;
    background: var(--edge-grey);
  }
  .card-back {
    position: relative;
    width: 1200px;
    height: 705px;
    overflow: hidden;
    background: var(--card-black);
  }
  .wave-art {
    position: absolute;
    inset: 0;
    width: 1200px;
    height: 705px;
  }
  .wave-art .deep { fill: var(--wave-deep); }
  .wave-art .bright { fill: var(--wave-bright); }
  .wave-art .light { fill: var(--wave-white); }
  .divider {
    position: absolute;
    left: 0;
    top: 350px;
    width: 1200px;
    height: 1px;
    background: var(--guide-grey);
  }
  .bottom-edge {
    position: absolute;
    left: 0;
    bottom: 0;
    width: 1200px;
    height: 6px;
    background: var(--edge-grey);
  }
  .services-title {
    position: absolute;
    left: 70px;
    top: 100px;
    margin: 0;
    font-family: "Open Sans", Arial, sans-serif;
    font-weight: 700;
    font-size: 82px;
    line-height: 1;
    color: var(--text-white);
  }
  .services-list {
    position: absolute;
    left: 0;
    top: 326px;
    width: 1192px;
    margin: 0;
    padding: 0;
    list-style: none;
    text-align: center;
    font-family: "Montserrat", Arial, sans-serif;
    font-weight: 400;
    font-size: 38px;
    line-height: 40px;
    letter-spacing: 0.4px;
    color: var(--text-white);
  }
  .services-list li::before {
    content: "";
    position: absolute;
    left: 107px;
    width: 11px;
    height: 11px;
    margin-top: 16px;
    border-radius: 50%;
    background: var(--text-white);
  }
</style>
</head>
<body>
  <main class="card-back">
    <svg class="wave-art" viewBox="0 0 1004 590" preserveAspectRatio="none" aria-hidden="true">
      <path class="light" d="M0,45 C80,25 250,5 400,35 C550,65 700,200 1004,242 V0 H0 Z"/>
      <path class="deep" d="M0,44 C80,24 250,3 400,31 C520,58 700,180 1004,214 V0 H0 Z"/>
      <path class="bright" d="M500,0 C610,70 760,128 1004,134 V0 Z"/>
      <path class="light" d="M410,0 C520,55 690,118 1004,92 V0 Z"/>
    </svg>

    <div class="divider"></div>

    <h1 class="services-title">Services</h1>

    <ul class="services-list">
      <li>Real Estate Sales and Investments</li>
      <li>Real Estate Rental Management</li>
      <li>Kitchen, Bathroom Reformations</li>
      <li>Complete Home Reformation Services</li>
      <li>Window and Door Replacement Landscape</li>
      <li>Garden Management</li>
      <li>Pool and Jacuzzi Service</li>
    </ul>

    <div class="bottom-edge"></div>
  </main>
</body>
</html>
```